Retirement Community Letterhead design needed to include our new logo

We recently updated our logo and need a new letterhead to go with it. Would like the letterhead to be clean, classic, and easy to read. I've attached our current logo and a copy of our old letterhead for reference.

If possible, we would like, "Living Well Together" to be included in someway.

Ashbrook Faith Meadows is a faith-based, not-for profit senior living community offering Independent Living, Assisted Living, and a Health Care Center.

Target Market(s)

45+ Women

Industry/Entity Type

Community

Colors
00a990

Requirements
Must have
• Must be clean and elegant.
• Font used must coordinate well with the Trajan Pro font in logo
Should not have
• No crazy graphics or details.

```html
<!DOCTYPE html>
<html lang="en">
<head>
<meta charset="utf-8">
<title>Ashbrook Faith Meadows – Letterhead</title>
<link rel="stylesheet" href="https://fonts.googleapis.com/css2?family=Cinzel:wght@500;600&family=Roboto:wght@400;500&display=swap">
<style>
  :root {
    --backdrop: #e9ebe9;
    --paper: #fafafa;
    --forest: #3f5c47;
    --leaf: #6fa33f;
    --ink: #3a4a3f;
    --mist: #ededed;
  }
  * { box-sizing: border-box; margin: 0; padding: 0; }
  html, body { width: 1200px; height: 1200px; overflow: hidden; }
  body {
    background: var(--backdrop);
    display: flex; align-items: center; justify-content: center;
    font-family: "Roboto", Arial, sans-serif;
  }
  .letterhead {
    position: relative;
    width: 720px; height: 1018px;
    background: var(--paper);
    box-shadow: 0 4px 18px rgba(0,0,0,.12);
    overflow: hidden;
  }
  .header-band {
    position: absolute; top: 0; left: 0; width: 100%; height: 150px;
    background: var(--forest);
  }
  .header-rule {
    position: absolute; top: 150px; left: 0; width: 100%; height: 6px;
    background: var(--leaf);
  }
  .brand-name {
    position: absolute; top: 52px; right: 52px;
    font-family: "Cinzel", "Times New Roman", serif;
    font-weight: 600; font-size: 17px; letter-spacing: 1.5px;
    color: #ffffff; text-align: right; line-height: 1.2;
  }
  .sender { position: absolute; top: 200px; left: 52px; color: var(--ink); }
  .sender-name {
    font-family: "Cinzel", "Times New Roman", serif;
    font-weight: 600; font-size: 22px; letter-spacing: .5px; color: var(--forest);
  }
  .sender-title { font-size: 13px; margin-top: 2px; }
  .contact-list { list-style: none; margin-top: 22px; font-size: 12.5px; line-height: 1.45; }
  .contact-list li { display: flex; align-items: flex-start; gap: 10px; }
  .contact-list svg { width: 12px; height: 12px; margin-top: 3px; flex: none; }
  .contact-list .address { display: block; }
  .landscape-decor {
    position: absolute; left: 0; bottom: 120px; width: 100%; height: 250px;
    background: linear-gradient(to bottom, rgba(237,237,237,0) 0%, var(--mist) 70%, rgba(237,237,237,0) 100%);
  }
  .tagline {
    position: absolute; bottom: 48px; left: 0; width: 100%;
    text-align: center; font-size: 15px; letter-spacing: 5px; color: var(--ink);
  }
</style>
</head>
<body>
  <main class="letterhead">
    <div class="header-band" aria-hidden="true"></div>
    <div class="header-rule" aria-hidden="true"></div>

    <div class="brand-name">Ashbrook<br>Faith Meadows</div>

    <section class="sender">
      <h1 class="sender-name">Daniel Whitford</h1>
      <p class="sender-title">Executive Director</p>
      <ul class="contact-list">
        <li>
          <svg viewBox="0 0 24 24"><path fill="var(--forest)" d="M6.6 10.8a15 15 0 0 0 6.6 6.6l2.2-2.2c.3-.3.7-.4 1-.2 1.1.4 2.3.6 3.6.6.6 0 1 .4 1 1V20c0 .6-.4 1-1 1A17 17 0 0 1 3 4c0-.6.4-1 1-1h3.5c.6 0 1 .4 1 1 0 1.3.2 2.5.6 3.6.1.3 0 .7-.2 1z"/></svg>
          <span>(555) 204-3187</span>
        </li>
        <li>
          <svg viewBox="0 0 24 24"><rect x="4" y="8" width="16" height="11" rx="2" fill="var(--forest)"/><rect x="7" y="3" width="10" height="6" fill="var(--forest)"/><rect x="7" y="14" width="10" height="5" fill="#fff"/></svg>
          <span>(555) 204-3190</span>
        </li>
        <li>
          <svg viewBox="0 0 24 24"><path fill="var(--forest)" d="M12 2a7 7 0 0 0-7 7c0 5 7 13 7 13s7-8 7-13a7 7 0 0 0-7-7zm0 9.5A2.5 2.5 0 1 1 12 6.5a2.5 2.5 0 0 1 0 5z"/></svg>
          <span><span class="address">48 Maple Ridge Lane</span><span class="address">Fairview, Ohio 45100-2200</span></span>
        </li>
      </ul>
    </section>

    <div class="landscape-decor" role="img" aria-label="Faint decorative landscape of rolling hills with trees"></div>

    <p class="tagline">Living Well Together</p>
  </main>
</body>
</html>
```